Re-Design an adult education portal

I need support to re-design an adult education portal. Currently the customer has an incomplete website which should be prepared in a new format.
I have the idea how to realize, but I have no clue how to design it. The hard thing is to have a "beautiful" website with available logo and main color. I hope you can support me.

Name of Website: tovrenu (tovrenu.ch)
Content: adult eduction for adult in safety at work, mountain climbing, dog school. various courses in different areas. But on old webpage is hard to find the different possibilities.
main color: Ral 6011 (green) -> #6C7C59
logo: you see on top of website the logo (2 dogs and a mountain with a colour gradient).

new website: for new webpage I decided to have a navigation for each section of education. In the main area I would like to have some pictures to give an idea what content is behind. At the moment it looks terrible, so I decided to use you as support for me to make the webpage prettier :). And maybe you have an better idea how to make it great. -> current state of new web page: https://tovrenu.bask-om.ch/

Target Market(s)

adult eduction for adult in safety at work, mountain climbing, dog school

Number of Pages Required

1 page

Font styles to use
Serif
Sans Serif

Requirements
Must have
• As main color is set "Ral 6011" (green) -> #6C7C59

```html
<!DOCTYPE html>
<html lang="en">
<head>
<meta charset="utf-8">
<title>tovrenu – Your personal training and course partner</title>
<link href="https://fonts.googleapis.com/css2?family=Lora:wght@400;500&family=Work+Sans:wght@300;400;500&display=swap" rel="stylesheet">
<style>
:root{
  --green:#6c7c59;
  --dark:#4b4e3d;
  --footer:#484b3b;
  --cream:#faf1dc;
  --ink:#3c3f31;
  --line:#8e8f80;
}
*{box-sizing:border-box;margin:0;padding:0}
html,body{width:1200px;height:4035px;overflow:hidden}
body{background:var(--green);font-family:"Work Sans",sans-serif;color:var(--cream);position:relative}
.serif{font-family:"Lora",serif;font-weight:400}
.abs{position:absolute}
.btn{position:absolute;display:flex;align-items:center;justify-content:center;border-radius:14px;font-size:14px;letter-spacing:.06em;text-transform:uppercase}
.btn-cream{background:var(--cream);color:var(--ink)}
.btn-dark{background:var(--dark);color:var(--cream)}

/* nav */
.site-nav{position:absolute;top:0;left:0;width:1200px;height:75px;background:var(--green);z-index:2}
.brand{position:absolute;left:102px;top:21px;width:63px;height:32px;background:var(--cream);border-radius:2px;display:flex;align-items:center;justify-content:center;font-size:12px;color:var(--ink)}
.nav-links{position:absolute;right:102px;top:28px;display:flex;gap:30px;font-size:12px;list-style:none}

/* hero */
.hero{position:absolute;top:75px;left:0;width:1200px;height:645px;background:linear-gradient(100deg,#3d4a2e 0%,#6b6a45 30%,#9a5a2c 50%,#a6612c 62%,#2e3550 80%,#3e4a2e 100%)}
.hero h1{position:absolute;left:102px;top:252px;font-size:50px;line-height:64px;width:700px}
.hero p{position:absolute;left:102px;top:390px;width:520px;font-size:15px;line-height:18px}
.hero .btn{left:102px;top:455px;width:249px;height:48px}
.dots{position:absolute;left:560px;top:604px;display:flex;gap:12px}
.dots span{width:16px;height:16px;border-radius:50%;background:var(--cream)}
.dots span:first-child{opacity:.5}

.section-title{position:absolute;font-size:53px;line-height:64px}

/* course cards */
.course{position:absolute;top:833px;width:310px;height:502px;border-radius:12px;overflow:hidden;background:var(--cream)}
.course .head{height:48px;background:var(--dark);display:flex;align-items:center;justify-content:center;font-size:14px;letter-spacing:.05em}
.course .photo{height:235px}
.course .label{text-align:center;font-size:9px;color:#8b8b76;margin-top:15px;letter-spacing:.08em}
.course ul{list-style:none;text-align:center;color:var(--ink);font-size:14.5px;line-height:30px;margin-top:6px}
.course .foot{position:absolute;bottom:0;left:0;right:0;height:50px;background:var(--dark);display:flex;align-items:center;justify-content:center;font-size:14px;letter-spacing:.06em}

/* about */
.about p{position:absolute;left:102px;top:1574px;width:395px;font-size:14.3px;line-height:18.3px;font-weight:300}
.about-photo{position:absolute;left:569px;top:1507px;width:529px;height:331px;border:3px solid var(--cream);border-radius:6px;background:linear-gradient(180deg,#7d8e55 0%,#5e7a3a 40%,#6f9a3c 100%)}

/* trainers */
.trainer{position:absolute;top:2005px;width:454px;height:580px;background:var(--cream);border-radius:12px;overflow:hidden}
.trainer .head{height:55px;background:var(--dark);display:flex;align-items:center;justify-content:center;font-size:24px;letter-spacing:.03em}
.trainer .photo{margin:0 auto;width:359px;height:251px}
.trainer .label{text-align:center;font-size:9px;color:#8b8b76;margin-top:9px;letter-spacing:.08em}
.trainer ul{list-style:none;width:406px;margin:4px auto 0;color:var(--ink);font-size:14.2px;text-align:center}
.trainer li{height:34px;line-height:33px;border-bottom:1px solid var(--line)}
.trainer li:last-child{border-bottom:none}
.trainer li a{color:var(--ink);font-weight:500;text-decoration:underline}

/* dogs */
.dog{position:absolute;top:2679px;width:311px;height:420px;background:var(--cream);border-radius:12px;overflow:hidden}
.dog .head{height:55px;background:var(--dark);display:flex;align-items:center;justify-content:center;font-size:24px}
.dog .photo{height:236px}
.dog ul{list-style:none;text-align:center;color:var(--ink);font-size:14.5px;line-height:25.5px;margin-top:16px}

/* contact */
.contact-title{position:absolute;left:0;width:1200px;top:3167px;text-align:center;font-size:53px;line-height:64px}
.contact-intro{position:absolute;left:350px;width:500px;top:3314px;text-align:center;font-size:14.3px;line-height:17px;font-weight:300}
.field{position:absolute;height:49px;width:417px;background:var(--cream);border-radius:12px;font-size:10px;color:#8b8b76;padding:18px 18px}
.field.message{width:997px;height:166px}

/* footer */
.site-footer{position:absolute;left:0;top:3840px;width:1200px;height:195px;background:var(--footer)}
.footer-brand{position:absolute;left:569px;top:30px;width:63px;height:32px;background:var(--cream);border-radius:2px;display:flex;align-items:center;justify-content:center;font-size:12px;color:var(--ink)}
.footer-contact{position:absolute;top:96px;left:0;width:1200px;display:flex;justify-content:center;gap:58px;font-size:11.5px;align-items:center}
.footer-contact span{display:flex;align-items:center;gap:16px}
.footer-links{position:absolute;top:146px;left:0;width:1200px;display:flex;justify-content:center;gap:58px;font-size:9.5px;list-style:none;color:#d8d2bf}
</style>
</head>
<body>

<header class="site-nav">
  <div class="brand">tovrenu</div>
  <ul class="nav-links">
    <li>Mountain Training</li><li>Occupational Safety</li><li>First Aid</li><li>Dog School</li><li>CZV</li><li>Contact</li><li>About</li>
  </ul>
</header>

<section class="hero" role="img" aria-label="Photo of a red-brown dog sitting beside a woman in a fur-hooded jacket in a forest">
  <h1 class="serif">Your personal training and course partner.</h1>
  <p>We offer training tailored to your needs , target-oriented and tailored to your skills and knowledge .</p>
  <div class="btn btn-cream">Join us today</div>
  <div class="dots"><span></span><span></span><span></span><span></span></div>
</section>

<h2 class="section-title serif" style="left:0;width:1200px;text-align:center;top:745px">Learn with us.</h2>

<article class="course" style="left:102px">
  <div class="head">MOUNTAIN TRAINING</div>
  <div class="photo" role="img" aria-label="Climbing rope and carabiners on rock beside hiking boots" style="background:linear-gradient(160deg,#8a6a4e,#5f4a3a 50%,#a07c5c)"></div>
  <div class="label">COURSES OFFERED</div>
  <ul><li>Basic Summer Training</li><li>Ski Technique</li><li>Avalanche Courses</li><li>Alpine Rescue</li></ul>
  <div class="foot">LEARN MORE</div>
</article>
<article class="course" style="left:445px">
  <div class="head">DOG SCHOOL</div>
  <div class="photo" role="img" aria-label="Dog running through agility weave poles on green turf" style="background:linear-gradient(180deg,#2f4a2c,#3e7a3a 45%,#4c8e41)"></div>
  <div class="label">COURSES OFFERED</div>
  <ul><li>Theory before buying a dog</li><li>Puppy School</li><li>Avalanche Dog Training</li><li>Welding Training</li></ul>
  <div class="foot">LEARN MORE</div>
</article>
<article class="course" style="left:788px">
  <div class="head">OCCUPATIONAL SAFETY</div>
  <div class="photo" role="img" aria-label="Safety helmet hanging from a crane hook in an industrial hall" style="background:linear-gradient(160deg,#1e2a3c,#3a4a62 50%,#1a2230)"></div>
  <div class="label">COURSES OFFERED</div>
  <ul><li>Forklift Training</li><li>Personal protective equipment (PPE)</li><li>Ariel Work Platform</li><li>Material Control</li></ul>
  <div class="foot">LEARN MORE</div>
</article>

<div class="btn btn-dark" style="left:445px;top:1385px;width:310px;height:48px">View all courses</div>

<section class="about">
  <h2 class="section-title serif" style="left:102px;top:1500px">About Us.</h2>
  <p>In my professional career, I have repeatedly experienced situations that gave me the idea of giving every interested person basic knowledge that allows them to react correctly and with the necessary calm in an emergency. The pooling and combining of knowledge and skills from the various specialist areas gives people security and confidence in their actions. Our own experience has shown that the more professionally you are prepared for borderline situations, the more safely and successfully an emergency situation can be mastered and even lives can be saved.</p>
  <div class="btn btn-dark" style="left:102px;top:1792px;width:249px;height:48px">Learn more</div>
  <div class="about-photo" role="img" aria-label="The two trainers sitting in a mountain meadow with their three dogs"></div>
</section>

<h2 class="section-title serif" style="left:100px;top:1906px">Your Trainers.</h2>

<article class="trainer" style="left:100px">
  <div class="head">Lukas Ferrand</div>
  <div class="photo" role="img" aria-label="Portrait of the mountain guide in front of snowy peaks" style="background:linear-gradient(180deg,#8fa0b4,#c9d0d6 40%,#4b6a58)"></div>
  <div class="label">CERTIFICATIONS</div>
  <ul>
    <li>Certified mountain guide &amp; dipl. Snow sports instructor</li>
    <li>Qualified specialist in piste and rescue services</li>
    <li>Instructor for cable cars in Switzerland</li>
    <li>Avalanche dog handler &amp; trainer KWRO</li>
    <li>Emergency aid instructor</li>
    <li>BLS AED instructor SRC</li>
    <li><a>View More..</a></li>
  </ul>
</article>
<article class="trainer" style="left:647px">
  <div class="head">Nora Ferrand</div>
  <div class="photo" role="img" aria-label="Trainer in an orange jacket raising an ice axe on a summit" style="background:linear-gradient(180deg,#1f3e6c,#5f7fa6 45%,#c8622a 75%,#3a3a3a)"></div>
  <div class="label">CERTIFICATIONS</div>
  <ul>
    <li>Health specialist</li>
    <li>BLS AED instructor SRC</li>
    <li>Emergency aid instructor</li>
    <li>Examination expert NHB (National Dog Owner Certificate)</li>
    <li>Examination expert ATF (everyday suitable family dog)</li>
    <li>BEVET dog trainer</li>
    <li>huntress</li>
  </ul>
</article>

<article class="dog" style="left:100px">
  <div class="head">Akila</div>
  <div class="photo" role="img" aria-label="Small dachshund sitting on a snow vehicle" style="background:linear-gradient(180deg,#d9dde2,#6d6a64 55%,#2a2a2a)"></div>
  <ul><li>Litter Date: 06/05/2011</li><li>Family Dog</li><li>Welding Dog</li><li>Avalanche Dog C</li></ul>
</article>
<article class="dog" style="left:443px">
  <div class="head">Jil</div>
  <div class="photo" role="img" aria-label="Dachshund lying on straw between antlers" style="background:linear-gradient(160deg,#8a7a5a,#6a4a2c 50%,#9a8a66)"></div>
  <ul><li>Litter Date: 08/07/2015</li><li>Family Dog</li><li>Welding Dog</li><li>Avalanche Dog C</li></ul>
</article>
<article class="dog" style="left:786px">
  <div class="head">Heimo</div>
  <div class="photo" role="img" aria-label="Brown and white spaniel lying in green grass" style="background:linear-gradient(160deg,#9fc26a,#4e3a2c 50%,#7fa84e)"></div>
  <ul style="margin-top:14px"><li>Litter Date: 05/06/2018</li><li>Family Dog</li><li>Welding Dog</li><li>Avalanche Dog A</li></ul>
</article>

<h2 class="contact-title serif">We are happy to be at your disposal<br>Contact us!</h2>
<p class="contact-intro">Whether specific courses or questions about current courses. We are pleased to be available. Don't hesitate to contact us.</p>

<form>
  <div class="field" style="left:100px;top:3401px">Tell us your name</div>
  <div class="field" style="left:680px;top:3401px">Email Address</div>
  <div class="field" style="left:100px;top:3470px">Phone Number</div>
  <div class="field" style="left:680px;top:3470px">Theme</div>
  <div class="field message" style="left:100px;top:3537px">Tell us how we can help you</div>
  <div class="btn btn-dark" style="left:473px;top:3722px;width:249px;height:49px">Sumbit</div>
</form>

<footer class="site-footer">
  <div class="footer-brand">tovrenu</div>
  <div class="footer-contact">
    <span><svg width="16" height="16" viewBox="0 0 24 24" fill="#faf1dc"><path d="M6.6 10.8c1.4 2.8 3.8 5.1 6.6 6.6l2.2-2.2c.3-.3.7-.4 1-.2 1.1.4 2.3.6 3.6.6.6 0 1 .4 1 1V20c0 .6-.4 1-1 1C10.6 21 3 13.4 3 4c0-.6.4-1 1-1h3.5c.6 0 1 .4 1 1 0 1.3.2 2.5.6 3.6.1.3 0 .7-.2 1z"/></svg>+41 79 000 12 34</span>
    <span><svg width="14" height="18" viewBox="0 0 24 30" fill="#faf1dc"><path d="M12 0C5.4 0 0 5.4 0 12c0 9 12 18 12 18s12-9 12-18C24 5.4 18.6 0 12 0zm0 16.5a4.5 4.5 0 1 1 0-9 4.5 4.5 0 0 1 0 9z"/></svg>Tovrenu GmbH, Lindenweg 27, CH-3900 Brig</span>
    <span><svg width="17" height="14" viewBox="0 0 24 20" fill="#faf1dc"><path d="M22 0H2C.9 0 0 .9 0 2v16c0 1.1.9 2 2 2h20c1.1 0 2-.9 2-2V2c0-1.1-.9-2-2-2zm0 4-10 6L2 4V2l10 6 10-6z"/></svg>info@tovrenu.ch</span>
  </div>
  <ul class="footer-links"><li>Privacy Policy</li><li>Terms &amp; Conditions</li><li>Mission Statement</li><li>Certifications</li><li>Imprint</li></ul>
</footer>

</body>
</html>
```